Business Card for a Creative Technology based HR services company

Our company name is Leaf8, and we build large communities of HR (human resource) and finance personnels through our mobile platform, and we conduct lots of on-line and off-line activities to get everyone constantly connected. Behind all these, we will also provide on-site HR and finance contractors to our clients, plus a host of other HR-related services. No process in our company takes more than 5-steps.
Our company slogan: Shaping Your Tomorrow
Target Market(s)
All human resource (HR) and finance personnels, from new entrants to highly experienced senior professionals.
Industry/Entity Type
Finance
Colors
Designer to choose colors to be used in the design.
Look and feel
Each slider illustrates characteristics of the customer's brand and the style your logo design should communicate.

```html
<!DOCTYPE html>
<html lang="en">
<head>
<meta charset="utf-8">
<title>Leaf8 Business Card</title>
<link href="https://fonts.googleapis.com/css2?family=Roboto:wght@400;500;700&display=swap" rel="stylesheet">
<style>
  :root {
    --navy: #0f2a52;
    --navy-deep: #0b2247;
    --red: #d8161f;
    --paper: #e8e9ea;
    --paper-shape: #dcdee0;
    --ink: #1d2533;
    --backdrop: #f2f2f0;
  }
  * { margin: 0; padding: 0; box-sizing: border-box; }
  html, body {
    width: 1200px; height: 900px; overflow: hidden;
    background: var(--backdrop);
    font-family: "Roboto", Arial, sans-serif;
  }
  .stage { position: relative; width: 1200px; height: 900px; }
  .card {
    position: absolute; left: 320px;
    width: 560px; height: 320px;
    overflow: hidden;
    box-shadow: 0 6px 18px rgba(0,0,0,0.12);
  }

  /* Front */
  .card-front { top: 100px; background: var(--navy); }
  .card-front .decor-band {
    position: absolute; right: 0; top: 0;
    width: 200px; height: 100%;
    background: var(--navy-deep);
  }
  .brand-name {
    font-weight: 700; font-size: 64px; letter-spacing: -1px; line-height: 1;
  }
  .card-front .brand-name {
    position: absolute; left: 0; right: 0; top: 106px;
    text-align: center; color: #ffffff;
  }
  .slogan {
    position: absolute; left: 0; right: 0; top: 214px;
    text-align: center; color: #dfe4ee;
    font-size: 15px; letter-spacing: 3.5px; font-weight: 400;
  }

  /* Back */
  .card-back { top: 480px; background: var(--paper); color: var(--ink); }
  .card-back .decor-band {
    position: absolute; right: 0; top: 0;
    width: 250px; height: 100%;
    background: var(--paper-shape);
  }
  .card-back .brand-name {
    position: absolute; left: 36px; top: 76px;
    color: var(--navy); font-size: 58px;
  }
  .divider {
    position: absolute; left: 36px; top: 178px;
    width: 260px; height: 1.5px; background: var(--navy);
  }
  .address {
    position: absolute; left: 36px; top: 226px;
    font-size: 15px; line-height: 1.35; color: var(--ink);
    font-style: normal;
  }
  .address .web b { color: var(--navy); font-weight: 700; }
  .person { position: absolute; left: 326px; top: 64px; }
  .person-name {
    color: var(--navy); font-size: 19px; font-weight: 500; letter-spacing: 0.3px;
  }
  .person-role { font-size: 12.5px; margin-top: 3px; }
  .contacts {
    position: absolute; left: 326px; top: 138px;
    list-style: none; font-size: 13.5px; line-height: 1.45;
  }
  .contacts li { display: flex; gap: 8px; }
  .contacts .label { color: var(--navy); font-weight: 700; width: 14px; }
</style>
</head>
<body>
<main class="stage">
  <section class="card card-front">
    <div class="decor-band"></div>
    <p class="brand-name">Leaf8</p>
    <p class="slogan">SHAPING YOUR TOMORROW</p>
  </section>

  <section class="card card-back">
    <div class="decor-band"></div>
    <p class="brand-name">Leaf8</p>
    <div class="divider"></div>
    <address class="address">
      4127 Harlow Ave. Linden,<br>
      CA 90412<br>
      <span class="web">www.<b>leaf8</b>.com</span>
    </address>
    <div class="person">
      <p class="person-name">DANNY MORRISON</p>
      <p class="person-role">Operation Manager</p>
    </div>
    <ul class="contacts">
      <li><span class="label">T</span><span>(555) 21 604 38 12</span></li>
      <li><span class="label">M</span><span>(555) 48 712 90 36</span></li>
      <li><span class="label">E</span><span>danny@leaf8.com</span></li>
    </ul>
  </section>
</main>
</body>
</html>
```